Production company require television show pitch document cover design

We're StoneHarbor Pictures — a television production company based in Canberra, Australia — and we're pitching a television show idea at an upcoming conference. The show's called "Frontline Reef Patrols", and it's about an elite Tasmanian whale rescue team who race the clock to save the lives of charismatic megafauna. That's where you come in! We need the pitch document to be eye-catching and draw potential investors in to the story we're trying to tell. Are you up for it?

We need a fully designed A4 cover page.

I've attached the two page pitch document to give you an idea of what the show's about. I've also attached the two logos of the production companies involved, an example of a pitch document ("Restless Tides") and some images of beached whales (for inspiration).

There are a couple of things we specifically need on the cover page but otherwise you're free to get creative!
Updates

Project Deadline Extended
Reason: As it's a public holiday on Monday, we wouldn't have time to properly review designs and provide feedback, so we're extending the deadline by 5 days.

Target Market(s)

International broadcasters.

Industry/Entity Type

It Company

Font styles to use
Sans Serif

Requirements
Must have
• Both logos featured (usually at the bottom of the cover page).
Logline (or tagline) featured: "On watch 24/7, Tasmania’s elite Whale Rescue team race the clock to the save the lives of stranded giants wherever they may be on the island’s rugged coastline."
[Factual series] written in top right hand corner (see example pitch document).

```html
<!DOCTYPE html>
<html lang="en">
<head>
<meta charset="utf-8">
<title>Frontline Reef Patrols — Pitch Cover</title>
<link rel="stylesheet" href="https://fonts.googleapis.com/css2?family=Rubik+Dirt&family=Barlow+Semi+Condensed:wght@500;700&display=swap">
<style>
  :root {
    --red: #c8121b;
    --red-bright: #e01822;
    --red-deep: #9c0a12;
    --red-dark: #5e0509;
    --yellow: #ffe316;
    --black: #0b0202;
    --white: #ffffff;
  }
  * { margin: 0; padding: 0; box-sizing: border-box; }
  html, body { width: 848px; height: 1200px; overflow: hidden; background: var(--black); }
  .cover {
    position: relative;
    width: 848px;
    height: 1200px;
    overflow: hidden;
    background: var(--red);
  }
  .cover__bands { position: absolute; inset: 0; width: 848px; height: 620px; }
  .cover__format {
    position: absolute;
    right: 28px;
    top: 14px;
    font-family: "Barlow Semi Condensed", "Arial Narrow", sans-serif;
    font-weight: 700;
    font-size: 15px;
    letter-spacing: 1.5px;
    text-transform: uppercase;
    color: var(--white);
  }
  .cover__title { position: absolute; left: 0; top: 34px; width: 848px; height: 520px; }
  .cover__title text {
    font-family: "Rubik Dirt", "Impact", sans-serif;
    font-size: 146px;
    fill: var(--yellow);
  }
  .cover__title .title-shadow { fill: var(--black); }
  .cover__photo {
    position: absolute;
    left: 0;
    top: 530px;
    width: 848px;
    height: 470px;
    background:
      radial-gradient(ellipse 42% 30% at 52% 38%, rgba(70,4,8,0.75) 0%, rgba(70,4,8,0) 100%),
      radial-gradient(ellipse 60% 22% at 40% 78%, rgba(90,5,10,0.7) 0%, rgba(90,5,10,0) 100%),
      radial-gradient(ellipse 30% 25% at 12% 55%, rgba(230,30,40,0.55) 0%, rgba(230,30,40,0) 100%),
      linear-gradient(to bottom, #8a0810 0%, #b20e18 14%, #7c070e 20%, var(--red-bright) 30%, #c0111b 60%, #8e0911 100%);
  }
  .cover__fade {
    position: absolute;
    left: 0;
    top: 520px;
    width: 848px;
    height: 680px;
    background:
      linear-gradient(to bottom, rgba(11,2,2,0.85) 0px, rgba(11,2,2,0) 40px, rgba(11,2,2,0) 380px, rgba(11,2,2,0.92) 450px, var(--black) 520px);
  }
  .cover__logline {
    position: absolute;
    left: 84px;
    top: 960px;
    width: 680px;
    font-family: "Barlow Semi Condensed", "Arial Narrow", sans-serif;
    font-weight: 700;
    font-size: 23px;
    line-height: 1.22;
    letter-spacing: 0.3px;
    text-transform: uppercase;
    text-align: center;
    color: var(--yellow);
  }
  .cover__credits {
    position: absolute;
    right: 40px;
    top: 1130px;
    display: flex;
    align-items: center;
    gap: 22px;
    font-family: "Barlow Semi Condensed", "Arial Narrow", sans-serif;
    color: var(--white);
  }
  .credits__label { font-weight: 500; font-size: 16px; }
  .partner { display: flex; align-items: center; gap: 8px; font-weight: 700; font-size: 17px; line-height: 1; }
  .partner__mark { width: 30px; height: 30px; border: 2px solid var(--white); border-radius: 50%; }
</style>
</head>
<body>
<main class="cover">
  <svg class="cover__bands" viewBox="0 0 848 620" aria-hidden="true">
    <polygon points="0,0 848,0 848,36 0,52" fill="var(--red-deep)"/>
    <polygon points="0,180 848,160 848,200 0,224" fill="var(--red-deep)"/>
    <polygon points="0,350 848,322 848,362 0,392" fill="var(--red-deep)"/>
    <polygon points="0,490 848,466 848,540 0,560" fill="var(--red-dark)"/>
  </svg>

  <p class="cover__format">Factual series</p>

  <svg class="cover__title" viewBox="0 0 848 520" role="heading" aria-level="1" aria-label="Frontline Reef Patrols">
    <g class="title-shadow">
      <text x="54" y="140" textLength="752" lengthAdjust="spacingAndGlyphs">FRONTLINE</text>
      <text x="108" y="312" textLength="652" lengthAdjust="spacingAndGlyphs">REEF</text>
      <text x="54" y="484" textLength="752" lengthAdjust="spacingAndGlyphs">PATROLS</text>
    </g>
    <text x="46" y="132" textLength="752" lengthAdjust="spacingAndGlyphs">FRONTLINE</text>
    <text x="100" y="304" textLength="652" lengthAdjust="spacingAndGlyphs">REEF</text>
    <text x="46" y="476" textLength="752" lengthAdjust="spacingAndGlyphs">PATROLS</text>
  </svg>

  <div class="cover__photo" role="img" aria-label="Red-toned photograph of a rescue crew in helmets aboard an inflatable rescue boat speeding across the water"></div>
  <div class="cover__fade" aria-hidden="true"></div>

  <p class="cover__logline">On watch 24/7, Tasmania’s elite whale rescue team race the clock to save the lives of stranded giants wherever they may be on the island’s rugged coastline.</p>

  <footer class="cover__credits">
    <span class="credits__label">A factual series by</span>
    <span class="partner"><span class="partner__mark"></span>StoneHarbor Pictures</span>
    <span class="partner">Tallow Films</span>
  </footer>
</main>
</body>
</html>
```